Architectural Design Brochure

I need you to design 5 pages (they will be used as templates which I can then edit later).

Please design 5 pages - copy the example pdf provided as reference (Kestrel Arc). Please copy pages 1,3,5,6,7 from the example provided. But make the style match my unique brand. I want the layout to be similar to the example but still must be unique - use my logo and brand style blue, white, silver and grey.

I must be able to edit the brochure myself after you have finished these 5 pages (to change text and images etc) so it must be given to me in suitable format which I can edit in (psd or gimp).

my website is www.plankwell.com.au
my logo is attached

Target Market(s)

Home Builders and Architects

Requirements
Must have
• I would like you to design it around my brand - white, blue, grey and silver.

Must do 5 pages, copy the layout as shown in the example Kestrel Arc pdf - I need pages 1,3,5,6,7
Nice to have
• Unique stlye
same layout as example - pages 1,3,5,6,7
Should not have
• Should not be exactly same style / watermarks etc as example

```html
<!DOCTYPE html>
<html lang="en">
<head>
<meta charset="utf-8">
<title>Brochure – Contents Page</title>
<link href="https://fonts.googleapis.com/css2?family=Jost:wght@300;400;500&display=swap" rel="stylesheet">
<style>
  :root {
    --stage: #2a2a2c;
    --brand-blue: #2a78bb;
    --brand-blue-deep: #1f64a3;
    --brand-blue-light: #4e93cf;
    --white: #ffffff;
    --silver-top: #f4f4f4;
    --silver-bottom: #d9dadc;
    --ink: #2b2b2b;
    --heading-blue: #2f7fc4;
    --rule: #8f9296;
  }
  html, body {
    margin: 0;
    padding: 0;
    width: 1112px;
    height: 1200px;
    overflow: hidden;
    background: var(--stage);
    font-family: "Jost", "Futura", sans-serif;
  }
  .canvas {
    position: relative;
    width: 1112px;
    height: 1200px;
  }
  .page {
    position: absolute;
    left: 156px;
    top: 35px;
    width: 800px;
    height: 1130px;
    background: var(--brand-blue);
    overflow: hidden;
    box-shadow: 0 20px 50px rgba(0,0,0,0.5);
  }
  .blueprint-art {
    position: absolute;
    left: 0;
    top: 0;
    width: 560px;
    height: 1130px;
    background:
      radial-gradient(ellipse at 30% 65%, rgba(110,160,215,0.45) 0%, rgba(80,140,205,0.2) 45%, rgba(42,120,187,0) 75%),
      linear-gradient(180deg, var(--brand-blue-deep) 0%, var(--brand-blue) 60%);
  }
  .page-number {
    position: absolute;
    right: -6px;
    top: -40px;
    font-weight: 300;
    font-size: 330px;
    line-height: 1;
    color: var(--white);
  }
  .page-label {
    position: absolute;
    right: 58px;
    top: 135px;
    font-weight: 400;
    font-size: 44px;
    color: var(--white);
    letter-spacing: 0.5px;
  }
  .contents-panel {
    position: absolute;
    left: 292px;
    top: 470px;
    width: 508px;
    height: 540px;
    background: linear-gradient(180deg, var(--silver-top) 0%, var(--white) 35%, var(--silver-bottom) 100%);
    box-shadow: -4px 6px 14px rgba(0,0,0,0.25);
  }
  .page-curl {
    position: absolute;
    left: 0;
    bottom: 0;
    width: 60px;
    height: 60px;
  }
  .contents-title {
    margin: 0;
    position: absolute;
    left: 48px;
    top: 38px;
    font-weight: 500;
    font-size: 72px;
    color: var(--heading-blue);
    letter-spacing: 0.5px;
  }
  .contents-list {
    list-style: none;
    margin: 0;
    padding: 0;
    position: absolute;
    left: 48px;
    right: 40px;
    top: 128px;
  }
  .contents-list li {
    position: relative;
    height: 40px;
  }
  .entry-title {
    display: block;
    text-align: right;
    font-size: 19px;
    color: var(--ink);
    padding-top: 10px;
    line-height: 24px;
    border-bottom: 1px solid var(--rule);
  }
  .entry-page {
    position: absolute;
    left: 0;
    top: 38px;
    font-size: 27px;
    line-height: 30px;
    color: var(--ink);
  }
</style>
</head>
<body>
<div class="canvas">
  <article class="page">
    <div class="blueprint-art" role="img" aria-label="Faint blueprint drawing of radiating guide lines, a measuring scale and a sweeping arc"></div>

    <div class="page-number">5</div>
    <div class="page-label">Page No.</div>

    <section class="contents-panel">
      <h1 class="contents-title">Contents</h1>
      <ol class="contents-list">
        <li><span class="entry-title">Introduction</span><span class="entry-page">3</span></li>
        <li><span class="entry-title">Who We Are</span><span class="entry-page">6</span></li>
        <li><span class="entry-title">The Directors</span><span class="entry-page">8</span></li>
        <li><span class="entry-title">Calvin Marsh</span><span class="entry-page">9</span></li>
        <li><span class="entry-title">Lorraine Marsh</span><span class="entry-page">9</span></li>
        <li><span class="entry-title">Drafting Documentation</span><span class="entry-page">10</span></li>
        <li><span class="entry-title">Design &amp; Range Home Design</span><span class="entry-page">12</span></li>
        <li><span class="entry-title">3D Perspectives &amp; Presentations</span><span class="entry-page">13</span></li>
        <li><span class="entry-title">Multi-Residential &amp; Commercial</span><span class="entry-page">15</span></li>
      </ol>
      <svg class="page-curl" viewBox="0 0 60 60" aria-hidden="true">
        <polygon points="0,0 0,60 60,60" fill="var(--brand-blue)"/>
        <polygon points="0,0 60,60 12,52" fill="#e6e7e9"/>
      </svg>
    </section>
  </article>
</div>
</body>
</html>
```